HOME PAGE AND AND SECONDARY DESIGN FOR INTERNAL PAGES

Construction company looking for an easy to navagate professional serious greyscale website with a good clean feel simple clean menu and responsive friendly design. Our main clientele is commercial properties business owners and investors of rental properties. This website is going to be static HTML5 and would need multiple sizing files for clean fast rendering. Clean and accurate design files a must so if your experienced awesome modern greyscale designer let's get started I need this done as soon as possible.

Industry/Entity Type

construction, electrical, plumbing, commercial build outs

Number of Pages Required

2 page

Font styles to use
Sans Serif

Colors

Designer to choose only greyscale colors for use in the design.

Requirements
Must have
• Main Menu... Home, Services, Projects, About our team

```html
<!DOCTYPE html>
<html lang="en">
<head>
<meta charset="utf-8">
<title>Keystone Works of Texas</title>
<link href="https://fonts.googleapis.com/css2?family=Orbitron:wght@700;800&family=Roboto:wght@400;500;700&display=swap" rel="stylesheet">
<style>
:root{
  --ink:#1f2124;
  --dark:#2b2e33;
  --slate:#5c616a;
  --band:#6b717b;
  --text:#6a6d72;
  --light:#eff0f2;
  --line:#d5d7db;
  --white:#ffffff;
}
*{box-sizing:border-box;margin:0;padding:0}
html,body{width:1200px;height:4448px;overflow:hidden}
body{position:relative;font-family:'Roboto',sans-serif;color:var(--ink);background:var(--white)}
.abs{position:absolute}
.display{font-family:'Orbitron',sans-serif;font-weight:800;letter-spacing:1px}
.btn{position:absolute;display:flex;align-items:center;gap:8px;justify-content:center;border-radius:22px;font-size:12px;font-weight:700;text-transform:uppercase;letter-spacing:.3px}
.btn .dot{width:12px;height:12px;border-radius:50%;background:currentColor;position:relative}
.btn .dot::after{content:"";position:absolute;left:4px;top:3px;border-left:5px solid var(--slate);border-top:3px solid transparent;border-bottom:3px solid transparent}
.btn-solid{background:var(--slate);color:var(--white)}
.btn-ghost{background:var(--white);color:var(--ink);border:1px solid var(--ink)}
.btn-ghost .dot::after{border-left-color:var(--white)}
.photo{position:absolute}
.section-title{position:absolute;left:0;width:1200px;text-align:center;font-size:24px}

/* header */
.brand{left:110px;top:40px;display:flex;align-items:center;gap:10px}
.brand-mark{width:30px;height:30px;background:var(--ink);border-radius:50%}
.brand-name{font-size:16px;font-weight:700;line-height:1.15;color:var(--ink)}
.call{left:716px;top:18px;display:flex;gap:10px;align-items:center}
.call .ic{width:30px;height:30px;border-radius:50%;background:var(--slate)}
.call small{display:block;font-size:12px;font-weight:700}
.call strong{font-size:17px;font-weight:500}
.login{left:946px;top:32px;font-size:12px;color:var(--slate);font-weight:500}
.nav{left:381px;top:84px;display:flex;gap:28px;font-size:14px;color:var(--dark)}
.nav .on{font-weight:700;color:var(--ink)}
.social{left:940px;top:77px;display:flex;gap:9px}
.social span{width:30px;height:30px;border-radius:50%;background:var(--slate)}

/* hero */
.hero{left:0;top:123px;width:1200px;height:657px}
.hero-copy{left:109px;top:290px;color:var(--white)}
.hero-copy .kicker{font-size:19px;font-weight:700;margin-bottom:22px}
.hero-copy h1{font-size:44px;line-height:56px;font-weight:800}
.hero-copy p{font-size:14.5px;line-height:21px;margin-top:28px;width:430px}

/* about */
.about-text{left:629px;top:900px;width:456px}
.about-text h2{font-size:23px;margin-bottom:24px}
.about-text p{font-size:14.5px;line-height:25.8px;color:var(--text);text-align:justify}

/* services */
.services{left:0;top:1347px;width:1200px;height:621px;background:var(--light)}
.card{position:absolute;top:1487px;width:313px;height:390px;background:var(--white);border:2px solid var(--line);border-radius:10px;text-align:center}
.card .photo{left:4px;top:4px;width:301px;height:194px;border-radius:6px 6px 0 0}
.card h3{position:absolute;top:237px;width:100%;font-size:18px;font-weight:500}
.card .rule{position:absolute;left:143px;top:268px;width:24px;height:2px;background:var(--ink)}
.card p{position:absolute;left:22px;top:282px;width:265px;font-size:13px;line-height:21.5px;color:var(--text)}
.card .btn{left:95px;top:376px;width:122px;height:32px;font-size:11px}
.arrow{position:absolute;top:1663px;width:34px;height:34px;border:1px solid var(--line);border-radius:50%;background:var(--white)}

/* testimonials */
.quote{position:absolute;top:2150px;width:462px;height:314px;background:var(--white);border:2px solid var(--line);border-radius:12px}
.quote p{position:absolute;left:29px;top:60px;width:400px;font-size:14.5px;line-height:27.5px;color:var(--text);text-align:justify}
.quote .who{position:absolute;left:29px;top:222px;display:flex;gap:20px;align-items:center}
.quote .avatar{width:58px;height:58px;border-radius:50%}
.quote .who b{font-size:14px;display:block}
.quote .who span{font-size:13px;color:var(--text);font-weight:500}
.quote .stars{position:absolute;right:28px;top:243px;font-size:13px;color:var(--slate);letter-spacing:2px}
.qmark{position:absolute;top:2102px;font-family:Georgia,serif;font-size:170px;line-height:1;color:var(--slate);font-weight:700}
.pager{left:570px;top:2518px;display:flex;gap:3px}
.pager span{width:10px;height:10px;border-radius:50%;background:var(--slate)}
.pager span.on{background:var(--white);border:1px solid var(--slate)}

/* blog */
.blog{left:0;top:2616px;width:1200px;height:656px}
.blog-grid{left:110px;top:2766px;width:975px;height:420px;background:var(--white)}
.post{position:absolute;width:325px;height:420px}
.post .date{position:absolute;background:var(--slate);color:var(--white);font-size:12px;font-weight:500;padding:8px 14px}
.post h4{position:absolute;left:24px;width:280px;font-size:14.5px;line-height:24px;font-weight:700}
.post p{position:absolute;left:24px;width:270px;font-size:12px;line-height:21px;color:var(--text)}
.post .more{position:absolute;left:24px;font-size:11.5px;font-weight:700;color:var(--slate);text-decoration:underline}

/* footer */
.footer{left:0;top:3923px;width:1200px;height:525px}
.footer-head{position:absolute;top:4056px;font-size:18px;font-weight:700;color:var(--white)}
.field{position:absolute;height:40px;border:1px solid #6f737a;border-radius:20px;color:var(--white);font-size:12.5px;padding:12px 20px}
.contact-row{position:absolute;left:573px;display:flex;gap:18px;align-items:center;color:var(--white);font-size:12.5px;line-height:19px}
.contact-row i{width:32px;height:32px;border-radius:50%;background:var(--white);flex:none}
.links{left:981px;top:4117px;color:var(--white);font-size:14px;line-height:30px;list-style:none}
.links li::before{content:"»";margin-right:18px}
.copy{left:0;top:4408px;width:1200px;text-align:center;font-size:13px;color:var(--white)}
</style>
</head>
<body>

<!-- Header -->
<div class="abs brand"><span class="brand-mark"></span><span class="brand-name">KEYSTONE WORKS<br>OF TEXAS LLC</span></div>
<div class="abs call"><span class="ic"></span><div><small>Call Us Today !</small><strong>555-014-2380</strong></div></div>
<div class="abs login">LOG IN &nbsp;/&nbsp; REGISTER</div>
<nav class="abs nav"><span class="on">HOME</span><span>SERVICES</span><span>PROJECTS</span><span>ABOUT</span><span>OUR TEAM</span><span>CONTACT US</span></nav>
<div class="abs social"><span></span><span></span><span></span><span></span></div>

<!-- Hero -->
<svg class="abs hero" viewBox="0 0 1200 657" role="img" aria-label="Modern white apartment building with a green lawn, in greyscale">
  <defs><linearGradient id="heroG" x1="0" x2="1" y1="0" y2="0"><stop offset="0" stop-color="#3a3d41"/><stop offset=".55" stop-color="#7d8187"/><stop offset="1" stop-color="#b9bbbe"/></linearGradient></defs>
  <polygon points="0,0 1200,0 1200,544 600,657 0,544" fill="url(#heroG)"/>
  <polygon points="0,544 600,657 1200,544 1200,560 600,660 0,560" fill="#5c616a"/>
</svg>
<div class="abs hero-copy">
  <div class="kicker">WELCOME TO</div>
  <h1 class="display">KEYSTONE WORKS<br>OF TEXAS</h1>
  <p>Sed uted perspiciatis unde omnis isted natus error sited voluptatem accusantium doloremque laudantiumed.</p>
</div>
<a class="btn btn-solid" style="left:110px;top:546px;width:146px;height:44px">Get Started <span class="dot"></span></a>

<!-- About -->
<div class="abs" style="left:108px;top:872px;width:376px;height:308px;border:12px solid var(--slate);border-right:none;border-bottom:none"></div>
<div class="abs" style="left:122px;top:885px;width:436px;height:380px;background:var(--white);border:1px solid var(--line)"></div>
<div class="photo" style="left:130px;top:893px;width:426px;height:369px;background:linear-gradient(135deg,#2a2c30,#777b80 60%,#c7c9cc)" role="img" aria-label="Person signing a property contract beside a small model house"></div>
<div class="abs about-text">
  <h2 class="display">ABOUT US</h2>
  <p>Lorem ipsum dolor sit amet, consectetur adipiscing elit, sed do eiusmod tempor incididunt ut labore et dolore magna aliqua. Ut enim ad minim veniam, quis nostrud exercitation ullamco laboris nisi ut aliquip ex ea commodo consequat. Duis aute irure dolor in reprehenderit in voluptate velit esse cillum dolore eu fugiat nulla pariatur. Excepteur sint occaecat cupidatat non proident, sunt in culpa qui officia deserunt mollit anim id est laborum Sed ut perspiciatis unde omnis iste natus error sit voluptatem accusantium doloremque laudantium, totam rem aperiam,</p>
</div>
<a class="btn btn-solid" style="left:629px;top:1213px;width:147px;height:44px">Learn More <span class="dot"></span></a>

<!-- Services -->
<div class="abs services"></div>
<h2 class="section-title display" style="top:1416px">OUR SERVICES</h2>
<span class="arrow" style="left:37px"></span>
<span class="arrow" style="left:1128px"></span>
<div class="card" style="left:107px"><div class="photo" style="background:linear-gradient(160deg,#d8d9db,#5d6066)" role="img" aria-label="Glass commercial office building"></div><h3>Commercial property</h3><span class="rule"></span><p>Lorem dolorsit consectetur adipiscingelit sed do eiusmod temporin cididuntut labore et dolore magna aliqua enimed.</p><a class="btn btn-ghost">Read More <span class="dot"></span></a></div>
<div class="card" style="left:442px"><div class="photo" style="background:linear-gradient(160deg,#4a4d52,#a9abae)" role="img" aria-label="Hands passing a small model house"></div><h3>Rental property</h3><span class="rule"></span><p>Lorem dolorsit consectetur adipiscingelit sed do eiusmod temporin cididuntut labore et dolore magna aliqua enimed.</p><a class="btn btn-ghost">Read More <span class="dot"></span></a></div>
<div class="card" style="left:779px"><div class="photo" style="background:linear-gradient(160deg,#c5c7ca,#55585d)" role="img" aria-label="Engineers on a construction site with cranes"></div><h3>Lorem ipsum dolor sit amet</h3><span class="rule"></span><p>Lorem dolorsit consectetur adipiscingelit sed do eiusmod temporin cididuntut labore et dolore magna aliqua enimed.</p><a class="btn btn-ghost">Read More <span class="dot"></span></a></div>

<!-- Testimonials -->
<h2 class="section-title display" style="top:2053px">WHAT OUR CLIENTS SAY</h2>
<div class="quote" style="left:110px"><p>Lorem ipsum dolor sit amet, consectetur adipiscing elit, sed do eiusmod tempor incididunt ut labore et dolore magna aliqua. Ut enim ad minim veniam, quis nostrud exercitation ullamco laboris nisi ut aliquip ex ea commodo consequat. Duis aute irure dolor in reprehenderit</p><div class="who"><span class="avatar" style="background:#4b4e53" role="img" aria-label="Client portrait"></span><div><b>DALE MORTON</b><span>Businessman</span></div></div><span class="stars">★★★★★</span></div>
<div class="quote" style="left:604px"><p style="font-style:italic">Lorem ipsum dolor sit amet, consectetur adipiscing elit, sed do eiusmod tempor incididunt ut labore et dolore magna aliqua. Ut enim ad minim veniam, quis nostrud exercitation ullamco laboris nisi ut aliquip ex ea commodo consequat. Duis aute irure dolor in reprehenderit</p><div class="who"><span class="avatar" style="background:#c9cbce" role="img" aria-label="Client portrait"></span><div><b>DALE MORTON</b><span>Businessman</span></div></div><span class="stars">★★★★★</span></div>
<div class="quote" style="left:1100px;opacity:.35"><p>Lorem ipsum dolor sit amet</p></div>
<div class="qmark" style="left:150px">“</div>
<div class="qmark" style="left:645px">“</div>
<div class="qmark" style="left:1140px;opacity:.3">“</div>
<div class="abs pager"><span></span><span></span><span class="on"></span><span></span><span></span></div>

<!-- Blog -->
<div class="abs blog" style="background:linear-gradient(180deg,#5f656e,#737983)" role="img" aria-label="Faint city street backdrop"></div>
<h2 class="section-title display" style="top:2699px;color:var(--white)">LATEST BLOG</h2>
<div class="abs blog-grid"></div>
<div class="post" style="left:110px;top:2766px">
  <div class="photo" style="left:5px;top:5px;width:318px;height:211px;background:linear-gradient(200deg,#e3e4e6,#3c3f44)" role="img" aria-label="Looking up at glass skyscrapers"></div>
  <span class="date" style="right:4px;top:5px">JUN 2023</span>
  <h4 style="top:256px">Lorem ipsum dolor sit amet, consec tetur adipiscing</h4>
  <p style="top:318px">Sed ut perspiciatis unde omnis iste natus error sit voluptatem accusantium doloremque</p>
  <span class="more" style="top:372px">LEARN MORE ➔</span>
</div>
<div class="post" style="left:435px;top:2766px">
  <h4 style="top:30px">Lorem ipsum dolor sit amet, consec tetur adipiscing</h4>
  <p style="top:92px">Sed ut perspiciatis unde omnis iste natus error sit voluptatem accusantium doloremque</p>
  <span class="more" style="top:144px">LEARN MORE ➔</span>
  <div class="photo" style="left:5px;top:208px;width:318px;height:208px;background:linear-gradient(160deg,#b5b7ba,#44474c)" role="img" aria-label="Modern office buildings beside trees"></div>
  <span class="date" style="left:115px;top:380px">JUN 2023</span>
</div>
<div class="post" style="left:760px;top:2766px">
  <div class="photo" style="left:5px;top:5px;width:318px;height:211px;background:linear-gradient(160deg,#8c8f94,#e4e5e7)" role="img" aria-label="Two colleagues reviewing plans at a desk"></div>
  <span class="date" style="right:4px;top:5px">JUN 2023</span>
  <h4 style="top:256px">Lorem ipsum dolor sit amet, consec tetur adipiscing</h4>
  <p style="top:318px">Sed ut perspiciatis unde omnis iste natus error sit voluptatem accusantium doloremque</p>
  <span class="more" style="top:372px">LEARN MORE ➔</span>
</div>

<!-- Projects -->
<h2 class="section-title display" style="top:3346px">OUR PROJECTS</h2>
<div class="photo" style="left:114px;top:3412px;width:318px;height:216px;background:linear-gradient(135deg,#2f3236,#9b9ea2)" role="img" aria-label="Signing papers beside a model house"></div>
<div class="photo" style="left:444px;top:3412px;width:155px;height:216px;background:linear-gradient(180deg,#d2d3d5,#4d5055)" role="img" aria-label="Apartment block with balconies"></div>
<div class="photo" style="left:609px;top:3412px;width:311px;height:216px;background:linear-gradient(180deg,#cfd0d3,#595c61)" role="img" aria-label="Workers at a building frame under construction"></div>
<div class="photo" style="left:929px;top:3412px;width:155px;height:216px;background:linear-gradient(135deg,#3b3e42,#b3b5b8)" role="img" aria-label="Hand holding house keys"></div>
<div class="photo" style="left:114px;top:3640px;width:318px;height:216px;background:linear-gradient(160deg,#a0a3a7,#35383c)" role="img" aria-label="Brick residential buildings"></div>
<div class="photo" style="left:440px;top:3640px;width:320px;height:216px;background:linear-gradient(160deg,#505358,#c2c4c7)" role="img" aria-label="Engineers reviewing blueprints on site"></div>
<div class="photo" style="left:768px;top:3640px;width:316px;height:216px;background:linear-gradient(160deg,#e5e6e8,#74777c)" role="img" aria-label="White modern house exterior"></div>

<!-- Footer -->
<svg class="abs footer" viewBox="0 0 1200 525">
  <polygon points="0,112 600,0 1200,112 1200,525 0,525" fill="#1f2124"/>
  <polygon points="0,112 600,0 1200,112 1200,96 600,-12 0,96" fill="#5c616a"/>
  <line x1="110" y1="457" x2="1088" y2="457" stroke="#55585d"/>
</svg>
<div class="footer-head" style="left:112px">Get In Touch</div>
<div class="field" style="left:112px;top:4117px;width:177px">Name</div>
<div class="field" style="left:300px;top:4117px;width:174px">Company</div>
<div class="field" style="left:112px;top:4176px;width:177px">Email</div>
<div class="field" style="left:300px;top:4176px;width:174px">Address</div>
<div class="field" style="left:112px;top:4235px;width:360px">Message</div>
<a class="btn btn-solid" style="left:114px;top:4297px;width:134px;height:40px">Submit Now</a>

<div class="footer-head" style="left:573px">Contact Us</div>
<div class="contact-row" style="top:4113px"><i></i><span>1200 RIDGELINE DRIVE STE 100<br>AUSTIN,TEXAS 78700</span></div>
<div class="contact-row" style="top:4165px"><i></i><span>555-014-2380</span></div>
<div class="contact-row" style="top:4216px"><i></i><span>KEYSTONEWORKSTX.COM</span></div>
<div class="contact-row" style="top:4268px"><i></i><span>info@keystoneworkstx.com</span></div>

<div class="footer-head" style="left:981px">Quick Links</div>
<ul class="abs links"><li>Home</li><li>Services</li><li>Projects</li><li>About</li><li>Our team</li><li>Contact Us</li></ul>

<div class="abs copy">© 2023 Keystone Works of Texas. &nbsp;|&nbsp; All Rights Reserved &nbsp;|</div>

</body>
</html>
```